Baby prediction and advice cards, thank you notes, Baby shower invitations and diaper raffle tickets

Please see attached brief with description of the project.

*** Only apply if you are DETAIL ORIENTED and willing to read 100% the brief and the correction instructions (if required)***

*** Only apply if you are able to communicate in English 100%***

We need QUALITY over quantity

Contact us if you have questions.

Thank you

Target Market(s)

Expecting mothers and their families (Mothers, sisters)

Font styles to use
Sans Serif

Colors

Designer to choose colors to be used in the design.

Requirements
Must have
• Read the brief
Should not have
• Read the brief

```html
<!DOCTYPE html>
<html lang="en">
<head>
<meta charset="utf-8">
<title>Baby Prediction and Advice Card Game</title>
<link rel="stylesheet" href="https://fonts.googleapis.com/css2?family=Open+Sans:wght@400;700&family=Quicksand:wght@300;400&display=swap">
<style>
  :root {
    --page: #ffffff;
    --heading: #8d6748;
    --card: #b4866a;
    --card-shade: #a97b5f;
    --chevron: #bf957b;
    --ink: #ffffff;
    --rule: rgba(255,255,255,0.8);
    --balloon-blue: #3aa0d8;
    --balloon-orange: #f4a42c;
    --balloon-yellow: #f6c25a;
    --sky: #a9d8f2;
    --sun: #f6a22a;
    --art-soft: rgba(255,255,255,0.55);
  }
  * { box-sizing: border-box; margin: 0; padding: 0; }
  html, body { width: 1200px; height: 562px; overflow: hidden; background: var(--page); }
  .sheet { position: relative; width: 1200px; height: 562px; }

  .sheet-title {
    position: absolute; left: 0; right: 0; top: 28px;
    text-align: center;
    font-family: "Open Sans", Arial, sans-serif;
    font-weight: 700; font-size: 36px; letter-spacing: 0.5px;
    color: var(--heading);
  }
  .side-label {
    position: absolute; width: 532px; text-align: center;
    font-family: "Open Sans", Arial, sans-serif; font-weight: 400;
    font-size: 31px; line-height: 40px; color: var(--heading);
  }
  .side-label--front { left: 38px; top: 504px; }
  .side-label--back { left: 632px; top: 492px; }

  .card {
    position: absolute; top: 104px; width: 532px; height: 382px;
    background: linear-gradient(160deg, var(--card) 0%, var(--card-shade) 100%);
    overflow: hidden;
  }
  .card--front { left: 38px; }
  .card--back { left: 632px; }
  .card__border { position: absolute; left: 5px; top: 5px; width: 522px; height: 372px; }

  .balloon-band {
    position: absolute; left: 0; right: 0; bottom: 0; height: 40px;
    background: linear-gradient(90deg, var(--balloon-orange), var(--balloon-blue) 18%, var(--balloon-yellow) 35%, var(--balloon-blue) 52%, var(--balloon-orange) 70%, var(--balloon-blue) 85%, var(--balloon-yellow));
  }

  .prediction-list { position: absolute; left: 30px; top: 20px; list-style: none; }
  .prediction {
    height: 24.25px; display: flex; align-items: center;
    font-family: "Quicksand", Arial, sans-serif; font-weight: 300; font-size: 13.5px;
    color: var(--ink); white-space: nowrap;
  }
  .prediction__bullet {
    width: 8px; height: 8px; border-radius: 50%; border: 1.5px solid var(--ink);
    margin-right: 10px; flex: none;
  }
  .prediction__label { display: inline-block; min-width: 90px; }
  .prediction__line { display: inline-block; height: 1px; background: var(--rule); margin-top: 9px; }

  .art { position: absolute; border-radius: 6px; }
  .art--sun-clouds { left: 386px; top: 20px; width: 128px; height: 88px; background: linear-gradient(135deg, var(--sky), var(--sun)); }
  .art--bottle { left: 442px; top: 148px; width: 44px; height: 52px; background: linear-gradient(var(--sky), var(--balloon-blue)); }
  .art--air-balloon { left: 450px; top: 256px; width: 50px; height: 72px; background: linear-gradient(var(--balloon-blue), var(--sky) 65%, var(--balloon-orange)); }

  .chevron-band { position: absolute; left: 0; right: 0; top: 128px; height: 216px; background: var(--chevron); opacity: 0.6; }
  .icon-art { position: absolute; background: var(--art-soft); border-radius: 8px; }
  .star { position: absolute; fill: var(--ink); }
</style>
</head>
<body>
<main class="sheet">
  <h1 class="sheet-title">BABY PREDICTION AND ADVICE CARD GAME</h1>

  <section class="card card--front" aria-label="Card front">
    <svg class="card__border" viewBox="0 0 522 372" aria-hidden="true">
      <rect x="2" y="2" width="518" height="380" rx="6" fill="none" stroke="#fff" stroke-width="3" stroke-linecap="round" stroke-dasharray="0 7"/>
    </svg>

    <ul class="prediction-list">
      <li class="prediction"><span class="prediction__bullet"></span><span class="prediction__label">Baby's name:</span><span class="prediction__line" style="width:206px"></span></li>
      <li class="prediction"><span class="prediction__bullet"></span><span class="prediction__label">Gender:</span><span class="prediction__line" style="width:206px"></span></li>
      <li class="prediction"><span class="prediction__bullet"></span><span class="prediction__label">Date of birth:</span><span class="prediction__line" style="width:206px"></span></li>
      <li class="prediction"><span class="prediction__bullet"></span><span class="prediction__label">Time of birth:</span><span class="prediction__line" style="width:206px"></span></li>
      <li class="prediction"><span class="prediction__bullet"></span><span class="prediction__label">Weight:</span><span class="prediction__line" style="width:206px"></span></li>
      <li class="prediction"><span class="prediction__bullet"></span><span class="prediction__label">Length:</span><span class="prediction__line" style="width:206px"></span></li>
      <li class="prediction"><span class="prediction__bullet"></span><span class="prediction__label">Hair Color:</span><span class="prediction__line" style="width:206px"></span></li>
      <li class="prediction"><span class="prediction__bullet"></span><span class="prediction__label">Eye Color:</span><span class="prediction__line" style="width:206px"></span></li>
      <li class="prediction"><span class="prediction__bullet"></span><span>Resemblance:&nbsp; All dad, All mom, both</span></li>
      <li class="prediction"><span class="prediction__bullet"></span><span>I hope you get mom's:&nbsp;</span><span class="prediction__line" style="width:240px"></span></li>
      <li class="prediction"><span class="prediction__bullet"></span><span>I hope you get dad's:&nbsp;</span><span class="prediction__line" style="width:206px"></span></li>
      <li class="prediction"><span class="prediction__bullet"></span><span>My best advice:&nbsp;</span><span class="prediction__line" style="width:292px"></span></li>
      <li class="prediction"><span class="prediction__bullet"></span><span>Best wishes and love from:&nbsp;</span><span class="prediction__line" style="width:206px"></span></li>
    </ul>

    <div class="art art--sun-clouds" role="img" aria-label="Illustration of a sun behind clouds"></div>
    <div class="art art--bottle" role="img" aria-label="Illustration of a baby bottle"></div>
    <div class="art art--air-balloon" role="img" aria-label="Illustration of a hot air balloon"></div>
    <div class="balloon-band" role="img" aria-label="Row of blue and orange balloons"></div>
  </section>

  <section class="card card--back" aria-label="Card back">
    <div class="chevron-band" role="img" aria-label="Soft chevron pattern"></div>
    <svg class="card__border" viewBox="0 0 522 372" aria-hidden="true">
      <rect x="2" y="2" width="518" height="380" rx="6" fill="none" stroke="#fff" stroke-width="3" stroke-linecap="round" stroke-dasharray="0 7"/>
    </svg>

    <svg class="star" style="left:50px;top:32px" width="26" height="26" viewBox="0 0 24 24" aria-hidden="true"><path d="M12 1l3.3 7 7.7.8-5.8 5.2 1.7 7.6L12 17.7 5.1 21.6l1.7-7.6L1 8.8 8.7 8z"/></svg>
    <svg class="star" style="left:206px;top:52px" width="18" height="18" viewBox="0 0 24 24" aria-hidden="true"><path d="M12 1l3.3 7 7.7.8-5.8 5.2 1.7 7.6L12 17.7 5.1 21.6l1.7-7.6L1 8.8 8.7 8z"/></svg>
    <svg class="star" style="left:312px;top:62px" width="10" height="10" viewBox="0 0 24 24" aria-hidden="true"><path d="M12 1l3.3 7 7.7.8-5.8 5.2 1.7 7.6L12 17.7 5.1 21.6l1.7-7.6L1 8.8 8.7 8z"/></svg>
    <svg class="star" style="left:406px;top:38px" width="14" height="14" viewBox="0 0 24 24" aria-hidden="true"><path d="M12 1l3.3 7 7.7.8-5.8 5.2 1.7 7.6L12 17.7 5.1 21.6l1.7-7.6L1 8.8 8.7 8z"/></svg>
    <svg class="star" style="left:456px;top:112px" width="26" height="26" viewBox="0 0 24 24" aria-hidden="true"><path d="M12 1l3.3 7 7.7.8-5.8 5.2 1.7 7.6L12 17.7 5.1 21.6l1.7-7.6L1 8.8 8.7 8z"/></svg>
    <svg class="star" style="left:40px;top:152px" width="26" height="26" viewBox="0 0 24 24" aria-hidden="true"><path d="M12 1l3.3 7 7.7.8-5.8 5.2 1.7 7.6L12 17.7 5.1 21.6l1.7-7.6L1 8.8 8.7 8z"/></svg>
    <svg class="star" style="left:76px;top:214px" width="14" height="14" viewBox="0 0 24 24" aria-hidden="true"><path d="M12 1l3.3 7 7.7.8-5.8 5.2 1.7 7.6L12 17.7 5.1 21.6l1.7-7.6L1 8.8 8.7 8z"/></svg>
    <svg class="star" style="left:30px;top:246px" width="16" height="16" viewBox="0 0 24 24" aria-hidden="true"><path d="M12 1l3.3 7 7.7.8-5.8 5.2 1.7 7.6L12 17.7 5.1 21.6l1.7-7.6L1 8.8 8.7 8z"/></svg>
    <svg class="star" style="left:168px;top:240px" width="14" height="14" viewBox="0 0 24 24" aria-hidden="true"><path d="M12 1l3.3 7 7.7.8-5.8 5.2 1.7 7.6L12 17.7 5.1 21.6l1.7-7.6L1 8.8 8.7 8z"/></svg>
    <svg class="star" style="left:424px;top:186px" width="12" height="12" viewBox="0 0 24 24" aria-hidden="true"><path d="M12 1l3.3 7 7.7.8-5.8 5.2 1.7 7.6L12 17.7 5.1 21.6l1.7-7.6L1 8.8 8.7 8z"/></svg>
    <svg class="star" style="left:476px;top:206px" width="22" height="22" viewBox="0 0 24 24" aria-hidden="true"><path d="M12 1l3.3 7 7.7.8-5.8 5.2 1.7 7.6L12 17.7 5.1 21.6l1.7-7.6L1 8.8 8.7 8z"/></svg>

    <div class="icon-art" style="left:252px;top:24px;width:36px;height:60px" role="img" aria-label="Baby rattle icon"></div>
    <div class="icon-art" style="left:456px;top:24px;width:40px;height:52px" role="img" aria-label="Baby socks icon"></div>
    <div class="icon-art" style="left:80px;top:76px;width:48px;height:68px" role="img" aria-label="Baby bib icon"></div>
    <div class="icon-art" style="left:404px;top:72px;width:48px;height:60px" role="img" aria-label="Safety pin icon"></div>
    <div class="icon-art" style="left:208px;top:120px;width:112px;height:108px" role="img" aria-label="Crib with star mobile icon"></div>
    <div class="icon-art" style="left:116px;top:204px;width:52px;height:48px" role="img" aria-label="Rubber duck icon"></div>
    <div class="icon-art" style="left:356px;top:188px;width:60px;height:64px" role="img" aria-label="Teddy bear icon"></div>
    <div class="icon-art" style="left:48px;top:276px;width:68px;height:60px" role="img" aria-label="Rocking horse icon"></div>
    <div class="icon-art" style="left:428px;top:268px;width:76px;height:64px" role="img" aria-label="Baby stroller icon"></div>

    <div class="balloon-band" role="img" aria-label="Row of blue and orange balloons"></div>
  </section>

  <p class="side-label side-label--front">Front</p>
  <p class="side-label side-label--back">Back</p>
</main>
</body>
</html>
```